Pastry Trade Institute Website Homepage Revision

I need the "homepage" to the new Northfield Pastry Trade Institute to reworked. The current homepage is dull. It needs the attention of a professional graphic artist so it delivers a professionally finished feel and look. I have included the current URL for your viewing (builds.vorlimo.com/bridal-torte/cms/ ) to see where we are in the development phase. The elements on the homepage are all necessary and the colors are correct. I have also included the original Word document for the page (you can extract the RGB values and images from the doc). To be clear, I am not looking to recreate all the web pages, just the homepage. It needs to be responsive and stretched.

Target Market(s)

All bakers who sell wedding cakes in the United States

Number of Pages Required

1 page

Font styles to use
Other font styles liked:
• see the Word Document

Requirements
Must have
• It must have the elements already in the original mock up. That includes the colors and fonts.

```html
<!DOCTYPE html>
<html lang="en">
<head>
<meta charset="utf-8">
<title>Northfield Pastry Trade Institute</title>
<link href="https://fonts.googleapis.com/css2?family=Lora:wght@400;500;700&family=Libre+Franklin:wght@600&display=swap" rel="stylesheet">
<style>
  :root {
    --pink: #ec2f7b;
    --teal: #17c3c5;
    --ink: #111111;
    --grey: #8a8a8a;
    --line: #e2e2e2;
    --yellow: #fcb900;
    --white: #ffffff;
    --outlet: #c4c4c4;
  }
  * { box-sizing: border-box; margin: 0; padding: 0; }
  html, body { width: 1200px; height: 1200px; overflow: hidden; background: var(--white); }
  body { position: relative; font-family: 'Lora', Georgia, serif; color: var(--ink); }
  .abs { position: absolute; }

  .brand { left: 176px; top: 44px; display: flex; align-items: center; gap: 8px; color: var(--pink); font-size: 17px; font-weight: 500; }
  .brand-dot { width: 14px; height: 14px; border-radius: 50%; background: var(--pink); }

  .menu-btn { left: 872px; top: 28px; width: 36px; height: 36px; border: 2px solid var(--pink); border-radius: 50%; display: flex; align-items: center; justify-content: center; }
  .login-btn { left: 923px; top: 28px; width: 102px; height: 36px; border: 2px solid var(--pink); border-radius: 18px; color: var(--pink); font-size: 15px; font-weight: 500; display: flex; align-items: center; justify-content: center; }

  .hero-title { left: 174px; top: 142px; font-size: 51px; line-height: 62px; font-weight: 400; letter-spacing: -0.5px; }
  .hero-title strong { font-weight: 700; display: block; font-size: 52px; }
  .hero-copy { left: 175px; top: 293px; width: 400px; font-size: 13.8px; line-height: 20.5px; }
  .discover-btn { left: 175px; top: 385px; width: 170px; height: 41px; border-radius: 21px; background: var(--pink); color: var(--white); font-size: 14.5px; font-weight: 500; display: flex; align-items: center; justify-content: center; gap: 14px; }

  .hero-photo { left: 632px; top: 104px; width: 394px; height: 366px; border-radius: 40% 40% 12px 12px / 30% 30% 12px 12px; background: radial-gradient(ellipse at 50% 55%, #f6efe4 0%, #e8d8c4 45%, #6b3a22 75%, #f3ece4 100%); }

  .rule { left: 0; top: 525px; width: 1200px; height: 1px; background: var(--line); }
  .seen-bar { left: 153px; top: 470px; width: 872px; height: 106px; border: 1.5px solid var(--line); border-radius: 12px; background: var(--white); }
  .seen-label { left: 178px; top: 500px; width: 125px; font-size: 17px; line-height: 25px; font-weight: 700; color: var(--grey); white-space: nowrap; }
  .seen-chevron { left: 308px; top: 470px; }
  .outlet { background: var(--outlet); }

  .video-panel { left: 153px; top: 621px; width: 510px; height: 433px; border-radius: 6px 0 0 6px; background: linear-gradient(135deg, #2e7f86 0%, #3ec9c6 45%, #7fe3dc 70%, #2a8f95 100%); overflow: hidden; }
  .quote-frame { left: 198px; top: 691px; width: 416px; height: 110px; border: 4px solid var(--white); border-radius: 6px; }
  .quote-mark { font-family: 'Lora', Georgia, serif; font-weight: 700; font-size: 92px; color: var(--white); line-height: 92px; height: 60px; overflow: hidden; }
  .quote-open { left: 218px; top: 668px; }
  .quote-close { left: 550px; top: 786px; }
  .watch-title { left: 198px; top: 720px; width: 416px; text-align: center; font-size: 35px; font-weight: 700; color: var(--white); }
  .click-btn { left: 306px; top: 838px; width: 206px; height: 62px; border-radius: 31px; background: var(--white); font-size: 23px; font-weight: 500; display: flex; align-items: center; justify-content: center; }

  .optin { left: 662px; top: 621px; width: 364px; height: 433px; border: 4px solid var(--teal); background: var(--white); }
  .optin-title { left: 700px; top: 655px; width: 285px; text-align: center; font-size: 24.5px; line-height: 34.5px; font-weight: 500; }
  .optin-title .big { font-size: 33px; font-weight: 700; }
  .field { left: 722px; width: 243px; height: 41px; border: 2px solid var(--ink); border-radius: 5px; font-size: 14px; padding-left: 17px; display: flex; align-items: center; }
  .field-name { top: 829px; }
  .field-email { top: 892px; }
  .watch-btn { left: 722px; top: 960px; width: 243px; height: 58px; border-radius: 29px; background: var(--yellow); font-size: 22px; font-weight: 500; display: flex; align-items: center; justify-content: center; gap: 22px; }

  .research-band { left: 0; top: 1105px; width: 1200px; height: 95px; background: var(--teal); overflow: hidden; }
  .research-line { position: absolute; left: 174px; top: 36px; font-size: 30.5px; color: var(--white); white-space: nowrap; }
  .research-caps { position: absolute; left: 174px; top: 87px; font-family: 'Libre Franklin', Arial, sans-serif; font-weight: 600; font-size: 34px; line-height: 34px; letter-spacing: 3px; color: var(--white); white-space: nowrap; }
</style>
</head>
<body>
  <div class="abs brand"><span class="brand-dot"></span>Northfield Pastry</div>

  <div class="abs menu-btn">
    <svg width="14" height="12" viewBox="0 0 14 12"><g stroke="#ec2f7b" stroke-width="2" stroke-linecap="round"><line x1="1" y1="2" x2="13" y2="2"/><line x1="1" y1="6" x2="13" y2="6"/><line x1="1" y1="10" x2="13" y2="10"/></g></svg>
  </div>
  <div class="abs login-btn">Login</div>

  <h1 class="abs hero-title">Be the best in<strong>Wedding Cakes</strong></h1>
  <p class="abs hero-copy">Take a tour with Us lorem ipsum dolor sit amet consectetur adip piscing dolor sit amet. If you are interested, contact Us anytime.</p>
  <div class="abs discover-btn">Discover more
    <svg width="18" height="14" viewBox="0 0 18 14"><g stroke="#fff" stroke-width="2" fill="none" stroke-linecap="round" stroke-linejoin="round"><line x1="1" y1="7" x2="16" y2="7"/><polyline points="10,1 16,7 10,13"/></g></svg>
  </div>

  <div class="abs hero-photo" role="img" aria-label="Two-tier white wedding cake with chocolate drip, fresh berries and chocolate-dipped strawberries on top"></div>

  <div class="abs rule"></div>
  <div class="abs seen-bar"></div>
  <div class="abs seen-label">IDA ROSS AS<br>SEEN ON</div>
  <svg class="abs seen-chevron" width="24" height="106" viewBox="0 0 24 106"><polyline points="1,0 1,34 22,53 1,72 1,106" fill="none" stroke="#e2e2e2" stroke-width="1.5"/></svg>

  <div class="abs outlet" style="left:360px;top:505px;width:50px;height:36px;border-radius:4px;"></div>
  <div class="abs outlet" style="left:461px;top:504px;width:41px;height:41px;"></div>
  <div class="abs outlet" style="left:548px;top:511px;width:68px;height:26px;border-radius:4px;"></div>
  <div class="abs outlet" style="left:661px;top:502px;width:45px;height:45px;border-radius:50%;"></div>
  <div class="abs outlet" style="left:755px;top:504px;width:38px;height:38px;border-radius:50%;"></div>
  <div class="abs outlet" style="left:838px;top:512px;width:65px;height:24px;border-radius:4px;"></div>
  <div class="abs outlet" style="left:938px;top:494px;width:58px;height:57px;"></div>

  <div class="abs video-panel" role="img" aria-label="Hands smoothing icing on a white tiered cake, tinted teal"></div>
  <div class="abs quote-frame"></div>
  <div class="abs quote-mark quote-open">“</div>
  <div class="abs quote-mark quote-close">”</div>
  <div class="abs watch-title">Watch This First</div>
  <div class="abs click-btn">Click Here</div>

  <div class="abs optin"></div>
  <h2 class="abs optin-title"><span class="big">How</span> a New Discovery Sells More Wedding Cakes and at Higher Prices!</h2>
  <div class="abs field field-name">Your First Name</div>
  <div class="abs field field-email">Your E-mail</div>
  <div class="abs watch-btn">WATCH NOW!
    <svg width="26" height="26" viewBox="0 0 26 26"><circle cx="13" cy="13" r="13" fill="#111"/><polygon points="10,7.5 19,13 10,18.5" fill="#fcb900"/></svg>
  </div>

  <section class="abs research-band">
    <p class="research-line">Our research is not just a game changer. It is the game changer.</p>
    <p class="research-caps">WE'RE REWRITING THE BOOK FOR SELLING</p>
  </section>
</body>
</html>
```